Harbor Ridge Holdings, LLC Business Card Design/Real Estate and Asset Mgmt.

Design business card with designer recommended colors using existing logo...teal color not mandatory. Business purpose is Asset Management and Real Estate.

The following text somewhere on the card:

HARBOR RIDGE HOLDINGS, LLC (llc can be very small font if needed.)
Tobias Welk CRB, SRS, CPM, CCIM (the abbreviations can be a smaller font)
PROPLICENSEE
517 Fenwick Lane #204-31
Alder Bluff, TN 37999
Toll Free: 888-555-0172
Cell: 931.555.0148
Email: tobiasrwelk@mailpost.example
www.harborridgeholdings.example

Target Market(s)

High net worth buyers and sellers. Will be providing commercial real estate sales and management services to banks and lenders who foreclose on bad debt collateral.

Industry/Entity Type

Real Estate

Contact Information for Business Card

Professional look. Maximum of two colors. Example: Logo one color and the text another. Or any combination the designer feels is appropriate.

Font styles to use
Other font styles liked:
• Designer's choice

Requirements
Must have
• Logo somewhere on the card.
Nice to have
• The card can be one sided or two sided or odd sized if the designer prefers.
• PROPLICENSEE Logo (small at the bottom or somewhere on the card. Even the back.)
Should not have
• Card should not be a folded card.

```html
<!DOCTYPE html>
<html lang="en">
<head>
<meta charset="utf-8">
<title>Harbor Ridge Holdings, LLC — Business Card</title>
<link href="https://fonts.googleapis.com/css2?family=EB+Garamond:wght@400&display=swap" rel="stylesheet">
<style>
  :root {
    --backdrop: #a9aaae;
    --card: #ffffff;
    --ink: #1c1c1c;
    --teal: #25a0b1;
  }
  * { margin: 0; padding: 0; box-sizing: border-box; }
  html, body { width: 1200px; height: 1000px; overflow: hidden; }
  body {
    background: var(--backdrop);
    position: relative;
    font-family: "EB Garamond", Garamond, Georgia, serif;
    font-weight: 400;
    color: var(--ink);
  }
  h1, h2 { font-weight: 400; }
  .card {
    position: absolute;
    left: 276px;
    width: 648px;
    height: 370px;
    background: var(--card);
  }
  .card--front { top: 86px; }
  .card--back { top: 518px; }

  .brand-mark {
    position: absolute;
    display: flex;
    align-items: center;
    color: var(--teal);
    white-space: nowrap;
  }
  .brand-mark__square { background: var(--teal); flex: none; }

  .front-mark { left: 0; width: 100%; top: 142px; justify-content: center; gap: 12px; font-size: 30px; }
  .front-mark .brand-mark__square { width: 18px; height: 18px; }

  .front-title {
    position: absolute; top: 200px; left: 0; width: 100%;
    text-align: center; font-size: 22px; letter-spacing: 0.2px;
  }
  .front-url {
    position: absolute; top: 230px; left: 0; width: 100%;
    text-align: center; font-size: 16px;
  }
  .llc { font-size: 12px; letter-spacing: 0.5px; }

  .back-title { position: absolute; left: 39px; top: 56px; font-size: 25px; letter-spacing: 0.3px; }
  .agent-name { position: absolute; left: 38px; top: 104px; font-size: 21px; }
  .agent-name__creds { font-size: 13px; }
  .agent-role { position: absolute; left: 37px; top: 129px; font-size: 14px; letter-spacing: 4px; }

  .rule { position: absolute; top: 151px; height: 2px; background: var(--teal); }
  .rule--left { left: 34px; width: 424px; }
  .rule--right { left: 502px; width: 112px; }

  .contact { position: absolute; left: 35px; top: 182px; font-size: 12px; line-height: 15.5px; }
  .contact p + p { margin-top: 16px; }

  .back-mark { left: 252px; top: 236px; gap: 14px; font-size: 34px; }
  .back-mark .brand-mark__square { width: 24px; height: 24px; }
</style>
</head>
<body>
  <section class="card card--front">
    <div class="brand-mark front-mark" role="img" aria-label="Harbor Ridge Holdings logo">
      <span class="brand-mark__square"></span>
      <span class="brand-mark__name">Harbor Ridge Holdings</span>
    </div>
    <h1 class="front-title">HARBOR RIDGE HOLDINGS, <span class="llc">LLC</span></h1>
    <p class="front-url">harborridgeholdings.example</p>
  </section>

  <section class="card card--back">
    <h2 class="back-title">HARBOR RIDGE HOLDINGS, <span class="llc">LLC</span></h2>
    <p class="agent-name">Tobias Welk <span class="agent-name__creds">CRB, SRS, CPM, CCIM</span></p>
    <p class="agent-role">PROPLICENSEE</p>
    <div class="rule rule--left"></div>
    <div class="rule rule--right"></div>
    <div class="contact">
      <p>517 Fenwick Lane #204-31<br>Alder Bluff, TN 37999</p>
      <p>Toll Free: 888-555-0172</p>
      <p>Cell: 931.555.0148<br>Email: tobiasrwelk@mailpost.example<br>www.harborridgeholdings.example</p>
    </div>
    <div class="brand-mark back-mark" role="img" aria-label="Harbor Ridge Holdings logo">
      <span class="brand-mark__square"></span>
      <span class="brand-mark__name">Harbor Ridge Holdings</span>
    </div>
  </section>
</body>
</html>
```